Webdesign for silver path

"Der Sternenpfad" is a new info product that will be selled through the website maybe you will create for us.

Translated from german to english the project is named "the silver path". It´s an online video course that teaches people how to live a fulfilling, happy and healthy life.

Design paramaters
We want a serious design that embodies the real feeling of beeing happy and fulfilled. Visitors should even feel good/better when they see the website.
In color psychology some sort of calming deep green like a four-leaf clover is recommend.
Mainly the website will be the external sales page with a big video as the central attention.
We also need a member area for customers to watch our video course.

So mainly we need a eye-cathing, calming header, the content body with mainly video and just a few written words...and of course a footer for links like imprint, affiliate program etc.

What we not want:
- some kind of these exaggerated smiling photos
- that bathetic luck symbols like money or boats
Updates

Hi,

i posted a message to the design discussion. Thank you!

Industry/Entity Type

Affiliate

```html
<!DOCTYPE html>
<html lang="en">
<head>
<meta charset="utf-8">
<title>the silver path</title>
<link href="https://fonts.googleapis.com/css2?family=Questrial&family=Roboto:wght@300;400&family=Sorts+Mill+Goudy&display=swap" rel="stylesheet">
<style>
:root{
  --green-deep:#066b2a;
  --green-panel:#1e7a26;
  --green-mid:#2f8f2c;
  --green-lime:#8cc21e;
  --green-pale:#b5d86a;
  --grey-bg:#d9d9d9;
  --text-body:#555;
  --text-nav:#3c3c3c;
  --player-dark:#151515;
  --player-bar:#222;
  --white:#fff;
}
*{margin:0;padding:0;box-sizing:border-box}
html,body{width:1200px;height:1190px;overflow:hidden}
body{
  position:relative;
  background:linear-gradient(180deg,#f4f4f4 0,#e9e9e9 300px,var(--grey-bg) 700px,#cfcfcf 1100px);
  font-family:"Roboto",sans-serif;
}
.site-header{position:absolute;left:0;top:0;width:1200px;height:140px;background:linear-gradient(180deg,#f1f1f1,#f7f7f7)}
.site-header::after{
  content:"";position:absolute;left:220px;right:200px;bottom:-14px;height:14px;
  background:radial-gradient(ellipse at top,rgba(0,0,0,.08),transparent 70%);
}
.brand{
  position:absolute;left:206px;top:58px;display:flex;align-items:center;gap:8px;
  font-family:"Questrial",sans-serif;font-size:36px;color:var(--green-mid);letter-spacing:-.5px;
}
.brand-dot{width:34px;height:34px;border-radius:50%;background:var(--green-mid)}
.member-tab{
  position:absolute;left:843px;top:0;width:140px;height:32px;
  background:var(--green-deep);border-radius:0 0 12px 12px;
  color:var(--white);font-family:"Questrial",sans-serif;font-size:15px;text-align:center;line-height:38px;
}
.member-tab::before{content:"";position:absolute;left:64px;top:5px;border:5px solid transparent;border-top-color:var(--white)}
.main-nav{position:absolute;left:600px;top:66px;display:flex;align-items:center;font-size:15px;color:var(--text-nav)}
.main-nav a{color:inherit;text-decoration:none}
.main-nav .active{display:block;width:76px;height:40px;line-height:40px;text-align:center;background:var(--green-mid);color:var(--white);margin-right:24px}
.main-nav .sep{color:var(--green-mid);margin:0 20px;font-size:13px}

.hero-art{
  position:absolute;left:0;top:250px;width:1200px;height:300px;
  background:linear-gradient(172deg,rgba(6,107,42,0) 8%,rgba(6,107,42,.75) 38%,rgba(47,143,44,.6) 55%,rgba(181,216,106,.45) 72%,rgba(181,216,106,0) 92%);
}
.hero-emblem{
  position:absolute;left:865px;top:290px;width:265px;height:265px;border-radius:50%;
  background:radial-gradient(circle,var(--green-deep) 0,var(--green-mid) 40%,var(--green-lime) 100%);
}

.hero-title{position:absolute;left:0;top:0;font-family:"Questrial",sans-serif;color:var(--green-deep);line-height:1}
.hero-kicker{position:absolute;left:386px;top:206px;font-size:31px;white-space:nowrap;letter-spacing:-.5px}
.hero-main{position:absolute;left:408px;top:236px;font-size:64px;white-space:nowrap;letter-spacing:-2px}
.hero-sub{position:absolute;left:523px;top:300px;font-size:41px;white-space:nowrap;letter-spacing:-1px}
.hero-sub .amp{color:#9a9a9a;font-family:"Sorts Mill Goudy",serif;font-size:60px;font-style:italic;line-height:0;vertical-align:-6px;margin:0 -2px}
.hero-author{
  position:absolute;left:568px;top:358px;width:224px;display:flex;align-items:center;justify-content:space-between;
  font-family:"Sorts Mill Goudy",serif;font-size:15px;color:#888;white-space:nowrap;line-height:18px;
}
.hero-author b{font-weight:normal;color:var(--green-deep)}
.hero-author .rule{width:34px;border-top:1px dotted #999}

.video-panel{position:absolute;left:227px;top:570px;width:746px;height:395px;background:var(--green-panel)}
.now-playing{position:absolute;left:26px;top:16px;font-family:"Sorts Mill Goudy",serif;font-weight:normal;font-size:17px;color:var(--white)}
.now-playing span{color:var(--green-pale);margin-right:6px}
.player{position:absolute;left:15px;top:51px;width:715px;height:328px;background:var(--player-dark)}
.player-screen{position:absolute;left:0;top:0;width:100%;height:274px}
.big-play{position:absolute;left:247px;top:30px}
.player-controls{position:absolute;left:0;bottom:0;width:100%;height:54px;background:var(--player-bar);color:#ddd;font-size:10px}
.player-controls svg{position:absolute}
.timecode{position:absolute;left:557px;top:22px;letter-spacing:.5px}
.intro{position:absolute;left:228px;top:983px;width:736px;font-size:11px;line-height:16px;color:var(--text-body)}
.site-footer{
  position:absolute;left:0;top:1111px;width:1200px;height:79px;
  background:linear-gradient(90deg,#5aa521 0,var(--green-deep) 20%,var(--green-deep) 80%,#5aa521 100%);
  color:var(--white);font-size:11.5px;
}
.footer-links{position:absolute;left:206px;top:35px}
.copyright{position:absolute;right:210px;top:35px}
</style>
</head>
<body>
<header class="site-header">
  <div class="brand"><span class="brand-dot"></span>the silver path</div>
  <a class="member-tab">Member Area</a>
  <nav class="main-nav">
    <a class="active">Home</a>
    <a>About Us</a><span class="sep">|</span>
    <a>Our Course</a><span class="sep">|</span>
    <a>Contact Us</a>
  </nav>
</header>

<div class="hero-art" role="img" aria-label="Flowing green wave ribbons with soft sparkles"></div>
<div class="hero-emblem" role="img" aria-label="Large green clover decoration"></div>

<div class="hero-title">
  <div class="hero-kicker">The cosmic sources of</div>
  <div class="hero-main">Self-knowledge</div>
  <div class="hero-sub">Love<span class="amp">&amp;</span>Partnership</div>
  <div class="hero-author"><span class="rule"></span><span>Author: <b>Lukas Hartmann</b></span><span class="rule"></span></div>
</div>

<section class="video-panel">
  <h2 class="now-playing"><span>Now Playing:</span>The Silver Path</h2>
  <div class="player">
    <div class="player-screen">
      <svg class="big-play" width="220" height="220" viewBox="0 0 220 220" aria-label="Play video">
        <defs>
          <radialGradient id="playGrad" cx=".5" cy=".35" r=".7">
            <stop offset="0" stop-color="#a6e23a"/><stop offset=".6" stop-color="#79c51e"/><stop offset="1" stop-color="#4f9a12"/>
          </radialGradient>
        </defs>
        <circle cx="110" cy="110" r="110" fill="#000"/>
        <circle cx="110" cy="110" r="102" fill="url(#playGrad)"/>
        <path d="M75,52 L175,110 L75,168 Z" fill="#fff"/>
      </svg>
    </div>
    <div class="player-controls">
      <svg style="left:14px;top:20px" width="14" height="14" viewBox="0 0 14 14"><circle cx="7" cy="7" r="6.5" fill="#ddd"/><path d="M4,4v6M10,4L5,7l5,3Z" stroke="#222" fill="#222"/></svg>
      <svg style="left:35px;top:12px" width="30" height="30" viewBox="0 0 30 30"><circle cx="15" cy="15" r="14" fill="#eee" stroke="#888"/><path d="M11,8 L22,15 L11,22Z" fill="#111"/></svg>
      <svg style="left:74px;top:20px" width="14" height="14" viewBox="0 0 14 14"><circle cx="7" cy="7" r="6.5" fill="#ddd"/><path d="M10,4v6M4,4l5,3l-5,3Z" stroke="#222" fill="#222"/></svg>
      <span class="timecode">00:00 / 00:00</span>
      <svg style="left:639px;top:22px" width="40" height="12" viewBox="0 0 40 12"><g fill="#9bb5d6"><rect x="0" y="10" width="2" height="2"/><rect x="4" y="9" width="2" height="3"/><rect x="8" y="8" width="2" height="4"/><rect x="12" y="7" width="2" height="5"/><rect x="16" y="6" width="2" height="6"/><rect x="20" y="4" width="2" height="8"/><rect x="24" y="3" width="2" height="9"/><rect x="28" y="2" width="2" height="10"/><rect x="32" y="1" width="2" height="11"/><rect x="36" y="0" width="2" height="12"/></g></svg>
      <svg style="left:689px;top:20px" width="14" height="12" viewBox="0 0 14 12"><rect x="0.5" y="0.5" width="13" height="11" fill="#9bb5d6" stroke="#ccd"/><rect x="2" y="3" width="10" height="1" fill="#fff"/><rect x="2" y="6" width="10" height="1" fill="#fff"/></svg>
    </div>
  </div>
</section>

<p class="intro">Only a few find what they crave. We all have the power sources in order to make our fortune really. The interconnectedness of humans with the cosmos has been scientifically proven and biophysicist Lukas Hartmann explains first how we can use the resulting energy for us. Why do we find it so difficult to be happy? Why do not we often succeed in finding the right partner and build strong relationships? The biophysicist Lukas Hartmann break new ground in order to answer these questions. He is convinced that until we find ourselves and our desire even then partner, if we go back to the cosmic source of life. ....</p>

<footer class="site-footer">
  <div class="footer-links">Home - About Us - Our Course - Imprint -&nbsp; Affiliate program - Contact Us</div>
  <div class="copyright">2012 The thesilverpath.com, Inc. All rights reserved,</div>
</footer>
</body>
</html>
```